Business Card/Stationary
General Contractor
Thank You for all of the submissions so far.
I have eliminated those that had too many curved lines. I like any lines to be more perpendicular/parallel. However, I have left a few with curved lines that I like.
I do like the solid colors on the front and or back.
I have not seen any stationary submissions. I need some of those as well, although not as critical as a business card.
Thank You for your submissions. I will comment again in a couple of days.

```html
<!DOCTYPE html>
<html lang="en">
<head>
<meta charset="utf-8">
<title>Halvern Builders, LLC — Stationery Set</title>
<link href="https://fonts.googleapis.com/css2?family=Questrial&family=Open+Sans:wght@400;600&display=swap" rel="stylesheet">
<style>
  :root{
    --board:#8b8b8b;
    --paper:#ffffff;
    --blue-deep:#1d3f8f;
    --blue-light:#4f86dd;
    --navy-rule:#0f2150;
    --orange:#f39a1e;
    --orange-deep:#e27a0f;
    --ink:#5a5a5a;
    --ink-soft:#8d8d8d;
    --card-note:#6b3f0a;
    --card-light:#e4ecfb;
  }
  *{box-sizing:border-box;margin:0;padding:0}
  html,body{width:1200px;height:662px;overflow:hidden;background:var(--board)}
  body{position:relative;font-family:"Open Sans",Arial,sans-serif;color:var(--ink)}
  .sheet{position:absolute;background:var(--paper);box-shadow:0 2px 6px rgba(0,0,0,.25);overflow:hidden}
  .band{position:absolute;left:0;right:0;top:0;background:linear-gradient(90deg,var(--blue-deep),var(--blue-light) 50%,var(--blue-deep));border-bottom:3px solid var(--navy-rule)}
  .brand{position:absolute;display:flex;align-items:center;gap:8px}
  .brand-square{background:var(--orange);flex:none}
  .brand-name{font-family:"Questrial",Arial,sans-serif;color:var(--ink);line-height:1;white-space:nowrap}
  .fine{font-size:6px;line-height:1.55;color:var(--ink-soft);position:absolute;white-space:nowrap}

  /* letterhead */
  .letterhead{left:200px;top:29px;width:456px;height:590px}
  .letterhead .band{height:26px}
  .letterhead .brand{left:26px;top:50px}
  .letterhead .brand-square{width:26px;height:26px}
  .letterhead .brand-name{font-size:22px}
  .letterhead .contact-left{left:26px;bottom:20px}
  .letterhead .contact-right{left:362px;bottom:20px}

  /* business cards */
  .card-back{left:20px;top:233px;width:172px;height:104px;background:linear-gradient(135deg,var(--orange),var(--orange-deep))}
  .card-back .fine{color:var(--card-note);left:92px;top:62px;font-size:5px}
  .card-front{left:20px;top:343px;width:172px;height:104px;display:flex}
  .card-front .half-white{width:40%;position:relative}
  .card-front .half-blue{flex:1;background:linear-gradient(135deg,var(--blue-light),var(--blue-deep));position:relative}
  .card-front .brand{left:7px;top:46px;gap:4px}
  .card-front .brand-square{width:11px;height:11px}
  .card-front .brand-name{font-size:8.5px}
  .card-front .holder{position:absolute;left:9px;top:10px;color:#fff;font-size:6px;line-height:1.4}
  .card-front .holder strong{font-weight:600;display:block}
  .card-front .half-blue .fine{color:var(--card-light);left:20px;top:56px;font-size:5px}

  /* envelope back */
  .envelope-back{left:662px;top:96px;width:495px;height:250px}
  .envelope-back svg{position:absolute;left:0;top:0}
  .envelope-back .brand{left:234px;top:50px}
  .envelope-back .brand-square{width:28px;height:28px}

  /* envelope front */
  .envelope-front{left:662px;top:352px;width:495px;height:205px}
  .envelope-front .band{height:16px}
  .envelope-front .brand{left:20px;top:40px}
  .envelope-front .brand-square{width:24px;height:24px}
  .envelope-front .brand-name{font-size:19px}
  .envelope-front .contact-left{left:20px;bottom:20px}
  .envelope-front .contact-right{left:390px;bottom:20px}
</style>
</head>
<body>

  <section class="sheet card-back" aria-label="Business card back">
    <p class="fine">Halvern Builders, LLC<br>General Contracting<br>Fenwick, Texas</p>
  </section>

  <section class="sheet card-front" aria-label="Business card front">
    <div class="half-white">
      <div class="brand"><span class="brand-square"></span><span class="brand-name">halvern</span></div>
    </div>
    <div class="half-blue">
      <p class="holder"><strong>Daniel R. Ostler</strong>President</p>
      <p class="fine">Tel: 555-014-2290<br>Cell: 555-014-2291<br>Fax: 555-014-2292<br>office@halvernbuilders.com</p>
    </div>
  </section>

  <section class="sheet letterhead" aria-label="Letterhead">
    <div class="band"></div>
    <div class="brand"><span class="brand-square"></span><span class="brand-name">halvern builders, llc</span></div>
    <p class="fine contact-left">office@halvernbuilders.com<br>4821 Marlow Crossing, Suite 12<br>Fenwick, TX 75501</p>
    <p class="fine contact-right">Tel: 555-014-2290<br>Cell: 555-014-2291<br>Fax: 555-014-2292</p>
  </section>

  <section class="sheet envelope-back" aria-label="Envelope back">
    <svg width="495" height="250" viewBox="0 0 495 250" aria-hidden="true">
      <defs>
        <linearGradient id="flapFill" x1="0" x2="1" y1="0" y2="0">
          <stop offset="0" stop-color="#1d3f8f"/>
          <stop offset=".5" stop-color="#4f86dd"/>
          <stop offset="1" stop-color="#1d3f8f"/>
        </linearGradient>
      </defs>
      <path d="M0 0H495V72Q495 96 471 96H24Q0 96 0 72Z" fill="url(#flapFill)"/>
      <path d="M0 72Q0 96 24 96H471Q495 96 495 72" fill="none" stroke="#0f2150" stroke-width="2"/>
    </svg>
    <div class="brand"><span class="brand-square"></span></div>
  </section>

  <section class="sheet envelope-front" aria-label="Envelope front">
    <div class="band"></div>
    <div class="brand"><span class="brand-square"></span><span class="brand-name">halvern builders, llc</span></div>
    <p class="fine contact-left">office@halvernbuilders.com<br>4821 Marlow Crossing, Suite 12<br>Fenwick, TX 75501</p>
    <p class="fine contact-right">Tel: 555-014-2290<br>Cell: 555-014-2291<br>Fax: 555-014-2292</p>
  </section>

</body>
</html>
```